New modern website for Kerbline Groundworks

Hi we are an existing company that has a current website http://www.kerblinegroundworks.co.nz/ we are looking to get a new vibrant looking website designed to take us further and gain more customers. We are after a simple easy to use website that does not confuse but we want to make an impact and stand out from the rest

Target Market(s)

Homeowners And Commercial Businesses

Industry/Entity Type

It Company

Coding

Coded - Design and coding required

Number of Pages Required

2 page

```html
<!DOCTYPE html>
<html lang="en">
<head>
<meta charset="utf-8">
<title>Kerbline Groundworks</title>
<link href="https://fonts.googleapis.com/css2?family=Jost:wght@400;500;600&family=Oswald:wght@500;700&display=swap" rel="stylesheet">
<style>
:root{
  --yellow:#f6b800;
  --yellow-deep:#e9a800;
  --dark:#2c2c2c;
  --darker:#1f1f1f;
  --ink:#222;
  --muted:#777;
  --light:#f1f1f1;
  --white:#fff;
  --band-grey:#9a9a9a;
}
*{box-sizing:border-box;margin:0;padding:0}
html,body{width:1200px;height:4196px;overflow:hidden}
body{font-family:"Jost",sans-serif;color:var(--ink);background:var(--white);position:relative}
.abs{position:absolute}
.btn{display:inline-block;background:var(--yellow);color:var(--ink);font-weight:600;font-size:13px;text-transform:uppercase;padding:6px 12px;border-radius:2px}

/* header */
.site-header{top:0;left:0;width:1200px;height:84px;background:var(--white)}
.brand{display:flex;align-items:center;gap:10px;font-weight:600;font-size:26px;color:var(--ink);letter-spacing:.5px;white-space:nowrap}
.brand-mark{width:14px;height:14px;background:var(--ink)}
.site-header .brand{position:absolute;left:100px;top:26px}
.main-nav{position:absolute;right:100px;top:28px;display:flex;gap:52px;font-size:16px}
.main-nav a{color:var(--ink);text-decoration:none;padding-bottom:6px}
.main-nav a.active{border-top:3px solid var(--yellow);padding-top:4px;margin-top:-7px}

/* hero */
.hero{top:84px;left:0;width:1200px;height:610px;background:linear-gradient(180deg,#cfdde6 0%,#b9c8c9 30%,#6f7a6a 48%,#44474a 70%,#2d2f31 100%)}
.hero-title{position:absolute;left:300px;top:372px;width:600px;text-align:center;font-family:"Oswald",sans-serif;font-weight:700;color:var(--white);font-size:36px;line-height:1.3;white-space:nowrap;text-shadow:0 2px 4px rgba(0,0,0,.5)}
.hero-title .accent{color:var(--yellow)}
.hero-arrow{position:absolute;top:330px;color:rgba(255,255,255,.7);font-size:26px}
.trust-bar{top:649px;left:98px;width:1002px;height:90px;background:var(--yellow);display:flex;align-items:center;justify-content:space-between;padding:0 42px}
.trust-bar p{font-size:20px}
.btn-outline{border:2px solid var(--ink);padding:10px 26px;font-weight:600;font-size:15px;text-transform:uppercase}

/* services */
.services{top:789px;left:98px;width:1002px;display:flex;justify-content:space-between}
.service-card{width:307px;height:358px;background:var(--white);box-shadow:0 1px 4px rgba(0,0,0,.15)}
.service-photo{height:198px;background:linear-gradient(180deg,#7d8a7e,#545450)}
.service-card h3{font-size:14px;font-weight:600;text-transform:uppercase;margin:18px 18px 6px}
.service-card p{font-size:13px;color:var(--muted);margin:0 18px 14px;line-height:1.4}
.service-card .btn{margin-left:18px}

/* plain bands */
.band{left:0;width:1200px}
.band-grey{background:var(--band-grey)}
.band-yellow{background:var(--yellow)}

/* welcome */
.welcome{top:1264px;left:0;width:1200px;height:542px;background:var(--dark);color:var(--white)}
.welcome-title{position:absolute;top:60px;left:0;width:1200px;display:flex;justify-content:center;align-items:center;gap:18px;font-size:28px;color:var(--yellow)}
.welcome-title .brand{color:var(--white);font-size:24px}
.welcome-title .brand-mark{background:var(--white)}
.video{position:absolute;left:100px;top:143px;width:482px;height:310px;background:linear-gradient(180deg,#8fa690,#5d6662 60%,#3a3c3d);border:3px solid #555}
.play{position:absolute;left:221px;top:135px;width:40px;height:40px;border-radius:50%;background:rgba(255,255,255,.5)}
.play:after{content:"";position:absolute;left:15px;top:11px;border-left:13px solid var(--dark);border-top:9px solid transparent;border-bottom:9px solid transparent}
.welcome-copy{position:absolute;left:626px;top:143px;width:470px}
.welcome-copy h2{font-size:20px;font-weight:500;line-height:1.35;margin-bottom:12px}
.welcome-copy p{font-size:14px;color:#b5b5b5;line-height:1.6;margin-bottom:14px}
.checks{list-style:none;margin-bottom:18px}
.checks li{display:flex;align-items:center;gap:12px;font-size:15px;margin-bottom:12px}
.tick{width:18px;height:18px;background:var(--yellow);display:flex;align-items:center;justify-content:center}

/* expertise */
.expertise{top:1832px;left:0;width:1200px;height:336px;background:linear-gradient(180deg,var(--yellow),var(--yellow-deep))}
.expertise h2{position:absolute;top:42px;width:1200px;text-align:center;font-size:30px;font-weight:500}
.expertise h2:after{content:"";display:block;width:200px;height:2px;background:var(--ink);margin:6px auto 0}
.badge{position:absolute;left:100px;top:148px;width:150px;height:150px;border-radius:50%;background:#1e1e1e;border:6px solid var(--yellow-deep);box-shadow:0 0 0 3px #1e1e1e}
.expertise p{position:absolute;left:334px;top:160px;width:770px;font-size:20px;line-height:1.5}

/* projects */
.section-title{width:1200px;text-align:center;font-size:32px;font-weight:500}
.section-title span{color:var(--yellow)}
.projects-grid{top:2299px;left:0;width:1200px;display:grid;grid-template-columns:repeat(4,300px);grid-auto-rows:274px}
.tile{position:relative}
.tile-overlay{position:absolute;inset:0;background:rgba(20,20,20,.55);color:var(--white);text-align:center;padding-top:78px}
.tile-overlay h3{font-size:22px;font-weight:500;margin-bottom:10px}
.tile-overlay p{font-size:13px;line-height:1.4;padding:0 50px}
.plus{width:42px;height:42px;border:2px solid var(--white);border-radius:50%;margin:22px auto 0;display:flex;align-items:center;justify-content:center;font-size:28px;line-height:1}
.view-all{top:2887px;left:483px;width:234px;height:42px;background:var(--yellow);border:2px solid #c78f00;font-weight:600;font-size:15px;display:flex;align-items:center;justify-content:center}

/* testimonials */
.testimonials{top:2982px;left:0;width:1200px;height:490px;background:var(--light)}
.testimonials .section-title{position:absolute;top:42px}
.testimonials .section-title:after{content:"";display:block;width:280px;height:2px;background:var(--ink);margin:6px auto 0}
.quotes{position:absolute;top:128px;left:98px;width:1004px;display:flex;justify-content:space-between}
.quote{width:320px;text-align:center}
.avatar{width:86px;height:86px;border-radius:50%;margin:0 auto;border:4px solid var(--yellow);background:linear-gradient(180deg,#d8c3b0,#8c7464)}
.quote h4{font-size:15px;font-weight:500;margin-top:14px}
.handle{font-size:12px;color:var(--yellow);margin-top:2px}
.quote-card{margin-top:22px;background:var(--white);padding:16px 20px;text-align:left;height:120px;box-shadow:0 1px 3px rgba(0,0,0,.12)}
.quote-card.featured{border:2px solid var(--yellow)}
.quote-card p{font-size:13px;color:var(--muted);line-height:1.4}
.quote-card small{display:block;font-size:10px;color:#aaa;margin-top:10px}

/* contact */
.ask{top:3492px;left:0;width:1200px;height:382px;background:linear-gradient(180deg,#d7c06a 0%,#c49a35 45%,#6e6a5e 100%)}
.ask-copy{position:absolute;left:100px;top:76px;width:300px;color:var(--white)}
.ask-copy h2{font-size:32px;font-weight:500;line-height:1.15;color:var(--ink);margin-bottom:16px}
.ask-copy p{font-size:13px;line-height:1.45;color:#3a3a3a}
.ask-form{position:absolute;left:458px;top:116px;width:643px;display:grid;grid-template-columns:306px 306px;gap:10px 30px}
.field{background:var(--white);height:42px;font-size:13px;padding:12px 14px;color:#666}
.submit{width:162px;height:40px;background:#111;color:var(--white);font-weight:600;font-size:15px;display:flex;align-items:center;justify-content:center;text-transform:uppercase}

/* footer */
.site-footer{top:3874px;left:0;width:1200px;height:266px;background:var(--darker);color:#bbb}
.col{position:absolute;top:38px}
.col h4{font-size:18px;font-weight:500;color:var(--white);margin-bottom:16px}
.col h4 span{color:var(--yellow)}
.col h4:after{content:"";display:block;width:80px;height:2px;background:#444;margin-top:6px}
.links{list-style:none;font-size:13px}
.links li{margin-bottom:9px}
.links li:before{content:"› ";color:var(--yellow)}
.links li.active{color:var(--yellow)}
.contact-list{list-style:none;font-size:13px}
.contact-list li{display:flex;gap:10px;margin-bottom:14px;line-height:1.35}
.map{width:272px;height:140px;background:linear-gradient(135deg,#b9cbe2,#dfe6d8)}
.site-footer .brand{position:absolute;left:852px;top:120px;color:var(--white);font-size:22px}
.site-footer .brand-mark{background:var(--white)}
.bottom-bar{top:4140px;left:0;width:1200px;height:56px;background:#141414;color:#888;font-size:12px;display:flex;align-items:center;justify-content:space-between;padding:0 100px}
.social{display:flex;gap:8px}
.social i{width:22px;height:22px;border-radius:50%;background:#3d8fd8;display:block}
</style>
</head>
<body>

<header class="abs site-header">
  <div class="brand"><span class="brand-mark"></span>Kerbline Groundworks</div>
  <nav class="main-nav">
    <a class="active">Home</a><a>About</a><a>Services</a><a>Projects</a><a>Contact Us</a>
  </nav>
</header>

<section class="abs hero" role="img" aria-label="Asphalt paving machine and crew laying a fresh road beside a tanker truck">
  <span class="hero-arrow" style="left:60px">‹</span>
  <span class="hero-arrow" style="right:60px">›</span>
  <h1 class="hero-title">Setting the standards for<br><span class="accent">QUALITY</span> Concrete &amp; Asphalters</h1>
</section>

<div class="abs trust-bar">
  <p>The trusted name for all Concrete &amp; Asphalt Paving in Auckland</p>
  <span class="btn-outline">Check out our work</span>
</div>

<section class="abs services">
  <article class="service-card">
    <div class="service-photo" role="img" aria-label="Workers raking hot asphalt"></div>
    <h3>Asphalt and concreting work</h3>
    <p>When it comes to all asphalt services, you can rest assured we will work around...</p>
    <span class="btn">Read more</span>
  </article>
  <article class="service-card">
    <div class="service-photo" role="img" aria-label="Labour crew in safety vests on a road site"></div>
    <h3>All labour</h3>
    <p>Guiding you throughout the process of our asphalt services, you can count on our...</p>
    <span class="btn">Read more</span>
  </article>
  <article class="service-card">
    <div class="service-photo" role="img" aria-label="Excavator digging red earth" style="background:linear-gradient(180deg,#8aa6c0,#b06a3c)"></div>
    <h3>Additional services</h3>
    <p>As part of our asphalt services, we are proud to offer a range of related services...</p>
    <span class="btn">Read more</span>
  </article>
</section>

<div class="abs band band-grey" style="top:1246px;height:18px"></div>

<section class="abs welcome">
  <div class="welcome-title">Welcome To <span class="brand"><span class="brand-mark"></span>Kerbline Groundworks</span></div>
  <div class="video" role="img" aria-label="Video still of a crew rolling a new asphalt driveway"><span class="play"></span></div>
  <div class="welcome-copy">
    <h2>Your one-stop specialist for driveway construction in Auckland</h2>
    <p>Leading the way for asphalt and concrete works throughout the Auckland region, Dean and the local team from Kerbline Groundworks will go the extra mile for your project.</p>
    <ul class="checks">
      <li><span class="tick"><svg width="12" height="12" viewBox="0 0 12 12"><path d="M2 6l3 3 5-6" stroke="#222" stroke-width="2" fill="none"/></svg></span>Personalized service</li>
      <li><span class="tick"><svg width="12" height="12" viewBox="0 0 12 12"><path d="M2 6l3 3 5-6" stroke="#222" stroke-width="2" fill="none"/></svg></span>Our expertise</li>
      <li><span class="tick"><svg width="12" height="12" viewBox="0 0 12 12"><path d="M2 6l3 3 5-6" stroke="#222" stroke-width="2" fill="none"/></svg></span>Our expertise</li>
    </ul>
    <span class="btn">Read more</span>
  </div>
</section>

<div class="abs band band-yellow" style="top:1806px;height:26px"></div>

<section class="abs expertise">
  <h2>Our Expertise</h2>
  <div class="badge" role="img" aria-label="Seventy years experience badge"></div>
  <p>We have a reputation with clients in and around Auckland for achieving great results on time and within budget every time. We are proud to share our years of experience.</p>
</section>

<h2 class="abs section-title" style="top:2214px">Latest <span>Projects</span></h2>
<section class="abs projects-grid">
  <div class="tile" role="img" aria-label="Concrete laying project" style="background:#6a6a5a">
    <div class="tile-overlay"><h3>Concrete laying</h3><p>Smooth finished slab poured for a new home entry.</p><div class="plus">+</div></div>
  </div>
  <div class="tile" role="img" aria-label="Garden path and lawn" style="background:linear-gradient(180deg,#4d6a3a,#7a8c5a)"></div>
  <div class="tile" role="img" aria-label="Paved brick driveway" style="background:linear-gradient(180deg,#6c7f4c,#8a6e5e)"></div>
  <div class="tile" role="img" aria-label="Paving machine with workers" style="background:linear-gradient(180deg,#b7c4cf,#5e5a50)"></div>
  <div class="tile" role="img" aria-label="Worker cutting concrete" style="background:linear-gradient(180deg,#7a7a72,#4a4c4a)"></div>
  <div class="tile" role="img" aria-label="New asphalt car park by the water" style="background:linear-gradient(180deg,#a9c2de,#4b4f53)"></div>
  <div class="tile" role="img" aria-label="Kerb and channel under construction" style="background:linear-gradient(180deg,#b6c7d9,#9a7a5c)"></div>
  <div class="tile" role="img" aria-label="Concrete retaining wall" style="background:linear-gradient(180deg,#7f9a5e,#9a9a94)"></div>
</section>
<div class="abs view-all">VIEW ALL PROJECTS</div>

<section class="abs testimonials">
  <h2 class="section-title"><span>Clients</span> Testimonials</h2>
  <div class="quotes">
    <div class="quote">
      <div class="avatar" role="img" aria-label="Client portrait"></div>
      <h4>Mr. Tane Whitford</h4><div class="handle">@twhitford</div>
      <div class="quote-card featured"><p>“ The crew arrived on time, kept the site tidy and left us with a driveway that looks superb.</p><small>4:24PM – MARCH 19, 2015</small></div>
    </div>
    <div class="quote">
      <div class="avatar" role="img" aria-label="Client portrait"></div>
      <h4>Miss Aria Penfold</h4><div class="handle">@apenfold</div>
      <div class="quote-card"><p>“ Clear pricing, friendly advice and a finished path we are proud of. Highly recommend them.</p><small>4:24PM – MARCH 19, 2015</small></div>
    </div>
    <div class="quote">
      <div class="avatar" role="img" aria-label="Client portrait"></div>
      <h4>Mr. Reuben Kahl</h4><div class="handle">@rkahl</div>
      <div class="quote-card"><p>“ Our car park was resurfaced within budget and with no fuss for our customers at all.</p><small>4:24PM – MARCH 19, 2015</small></div>
    </div>
  </div>
</section>

<div class="abs band band-grey" style="top:3472px;height:20px"></div>

<section class="abs ask" role="img" aria-label="Country road through golden fields under a yellow tint">
  <div class="ask-copy">
    <h2>Any Questions you would like to ask?</h2>
    <p>Send us a note about your driveway, path or car park and our team will reply within one working day with friendly advice and a free quote. [+]</p>
  </div>
  <div class="ask-form">
    <div class="field">Name</div><div class="field">Email</div>
    <div class="field">Phone</div><div class="field">Message</div>
    <div class="submit">Submit</div>
  </div>
</section>

<footer class="abs site-footer">
  <div class="col" style="left:100px">
    <h4><span>Quick</span> Links</h4>
    <ul class="links"><li class="active">Home</li><li>About</li><li>Services</li><li>Projects</li><li>Contact Us</li></ul>
  </div>
  <div class="col" style="left:264px">
    <h4>Contact <span>Details</span></h4>
    <ul class="contact-list">
      <li><svg width="12" height="14" viewBox="0 0 12 14"><path d="M6 0a5 5 0 0 0-5 5c0 4 5 9 5 9s5-5 5-9a5 5 0 0 0-5-5z" fill="var(--yellow)"/></svg>48 Harbourview Road,<br>Auckland 1010</li>
      <li><svg width="12" height="14" viewBox="0 0 12 14"><rect x="2" y="0" width="8" height="14" rx="1.5" fill="var(--yellow)"/></svg>021 555 0147</li>
      <li><svg width="12" height="14" viewBox="0 0 12 14"><path d="M2 1l3 0 1 3-2 1c1 2 2 3 4 4l1-2 3 1 0 3c-6 1-11-4-10-10z" fill="var(--yellow)"/></svg>09 555 0192</li>
      <li><svg width="12" height="14" viewBox="0 0 12 14"><rect x="0" y="3" width="12" height="8" fill="var(--yellow)"/></svg>info@kerblinegroundworks.co.nz</li>
    </ul>
  </div>
  <div class="col" style="left:530px">
    <h4><span>Location</span> Map</h4>
    <div class="map" role="img" aria-label="Street map showing the office location"></div>
  </div>
  <div class="brand"><span class="brand-mark"></span>Kerbline Groundworks</div>
</footer>

<div class="abs bottom-bar">
  <span>Copyright ©2016 Kerbline Groundworks . All Rights Reserved.</span>
  <div class="social"><i></i><i></i><i></i><i style="background:var(--yellow)"></i></div>
</div>

</body>
</html>
```